Plant Grower/Nursery needs a fun, professional and fresh 1/2 page print ad for a high profile gar...

We need a print ad for a garden tour geared towards plant enthusiasts that support California Native, natural and sustainable plants. A good percentage of our target market want a conservation and earth friendly approach to gardens/landscaping. We want to target this market, as well as, people who are looking for a pretty/colorful landscape that require little water/maintenance. **PLEASE LET US KNOW IF YOU HAVE QUESTIONS OR NEED MORE INFORMATION. WE ALSO HAVE MANY MORE PICTURES IF THESE DON'T WORK FOR YOUR DESIGN. ***THE AD CAN HAVE AS FEW AS 1 PHOTO - WE ARE POSTING SEVERAL IN HOPES THAT YOU CAN FIND WHAT IS PERFECT FOR YOUR IDEA!!Thank you

Target Market(s)

Gardeners, Landscapers, Landscape Designers/Architects, Cities and Municipalities.

Industry/Entity Type

Agriculture

Font styles to use
Serif
Sans Serif

Colors

Requirements
Must have
• We believe in growing regionally appropriate plants for Southern California that beatify our natural and urban landscapes.
• For over 20 years, our owners and staff take pride in providing timely, expert, and honest service.
Nice to have
• At least 1 photo. Eye catchy with a modern earthy feel.
• Hundreds of species/hybrids in stock of California Natives, Succulents, Ornamental Grasses, Standard Stock Items and Unique Plants.

```html
<!DOCTYPE html>
<html lang="en">
<head>
<meta charset="utf-8">
<title>Native Plant Nursery – Print Ad</title>
<link href="https://fonts.googleapis.com/css2?family=Montserrat:wght@600;700;800&family=Oswald:wght@300;400;500&display=swap" rel="stylesheet">
<style>
  :root {
    --paper: #ffffff;
    --mist: #e6e6e6;
    --leaf: #4f8a10;
    --leaf-light: #6aa51b;
    --leaf-dark: #3b6e0a;
    --ink: #262626;
    --accent: #d9821c;
    --bar: #333333;
  }
  * { margin: 0; padding: 0; box-sizing: border-box; }
  html, body { width: 1200px; height: 800px; overflow: hidden; background: #f2f2f2; }
  .ad {
    position: relative;
    width: 1200px;
    height: 800px;
    overflow: hidden;
    background: var(--paper);
    font-family: "Montserrat", sans-serif;
  }
  .ad__backdrop {
    position: absolute;
    left: 0; top: 0;
    width: 760px; height: 546px;
    background:
      radial-gradient(ellipse 260px 200px at 120px 140px, #d4d4d4 0%, rgba(230,230,230,0) 70%),
      radial-gradient(ellipse 300px 160px at 380px 330px, #dedede 0%, rgba(235,235,235,0) 75%),
      linear-gradient(90deg, #ececec 0%, #f7f7f7 60%, #ffffff 100%);
  }
  .ad__art { position: absolute; inset: 0; }
  .ad__logo {
    position: absolute;
    left: 225px; top: 34px;
    font-family: "Montserrat", sans-serif;
    font-weight: 800;
    font-size: 56px;
    letter-spacing: 1px;
    color: var(--ink);
  }
  .promise {
    position: absolute;
    left: 0; top: 427px;
    padding-left: 38px;
  }
  .promise__bar {
    position: absolute;
    left: 0; top: 0;
    width: 25px; height: 88px;
    background: var(--bar);
  }
  .promise__years {
    font-family: "Montserrat", sans-serif;
    font-weight: 600;
    font-size: 23px;
    line-height: 26px;
    color: var(--accent);
  }
  .promise__line {
    font-family: "Oswald", sans-serif;
    font-weight: 300;
    font-size: 21px;
    line-height: 26px;
    color: var(--ink);
    transform: scaleX(0.88);
    transform-origin: left;
    white-space: nowrap;
  }
  .promise__values {
    font-family: "Oswald", sans-serif;
    font-weight: 400;
    font-size: 29px;
    line-height: 34px;
    color: var(--ink);
    transform: scaleX(0.88);
    transform-origin: left;
    white-space: nowrap;
  }
  .belief {
    position: absolute;
    left: 38px; top: 578px;
    font-family: "Montserrat", sans-serif;
    font-weight: 700;
    font-size: 21px;
    line-height: 31px;
    color: #ffffff;
    white-space: nowrap;
  }
  .ad__footer {
    position: absolute;
    left: 0; top: 714px;
    width: 1200px; height: 86px;
    background: linear-gradient(90deg, #ececec 0%, #f9f9f9 40%, #e9e9e9 75%, #f4f4f4 100%);
  }
</style>
</head>
<body>
  <main class="ad">
    <div class="ad__backdrop" role="img" aria-label="Soft faded grey image of foliage"></div>

    <svg class="ad__art" width="1200" height="800" viewBox="0 0 1200 800" aria-hidden="false">
      <defs>
        <linearGradient id="bandGreen" x1="0" y1="0" x2="1" y2="0">
          <stop offset="0" stop-color="#4a840e"/>
          <stop offset="0.5" stop-color="#62a017"/>
          <stop offset="1" stop-color="#3f760b"/>
        </linearGradient>
        <radialGradient id="bloom" cx="0.55" cy="0.45" r="0.6">
          <stop offset="0" stop-color="#b98ac9"/>
          <stop offset="0.22" stop-color="#8f6a7a"/>
          <stop offset="0.5" stop-color="#4d6a33"/>
          <stop offset="1" stop-color="#2f4a1c"/>
        </radialGradient>
      </defs>
      <rect class="band" x="0" y="546" width="1200" height="168" fill="url(#bandGreen)"/>
      <ellipse class="photo-ring" cx="955" cy="240" rx="450" ry="428" fill="var(--leaf)"/>
      <ellipse class="photo" cx="963" cy="233" rx="440" ry="415" fill="url(#bloom)"
        role="img" aria-label="Photo of a purple native wildflower in bloom against green foliage"/>
    </svg>

    <div class="ad__logo">LOGO</div>

    <section class="promise">
      <span class="promise__bar"></span>
      <p class="promise__years">FOR OVER 20 YEARS,</p>
      <p class="promise__line">OUR OWNERS AND STAFF TAKE PRIDE IN PROVIDING</p>
      <p class="promise__values">TIMELY, EXPERT, AND HONEST SERVICE.</p>
    </section>

    <p class="belief">
      WE BELIEVE IN GROWING REGIONALLY<br>
      APPROPRIATE PLANTS FOR SOUTHERN CALIFORNIA<br>
      THAT BEATIFY OUR NATURAL AND URBAN LAND SCAPES
    </p>

    <div class="ad__footer"></div>
  </main>
</body>
</html>
```